Web design for Money Service Business (uncoded)

We need a very basic website with 5-6 pages. Home page, Services, Transfer(How to use our service), About us, Contact us, FAQ
Our company name is Meridale Exchange. We are a company that deals with currency exchange and international money transfer. We do cash exchange and international money transfers to bank accounts all over the world. We offer highly competitive exchange rates so usually attract customers who transfer money over $10,000. Our niche is with larger sums of money, the design needs to be professional and communicate trust, security and stability.

```html
<!DOCTYPE html>
<html lang="en">
<head>
<meta charset="utf-8">
<title>Meridale Exchange – International Money Transfer</title>
<link href="https://fonts.googleapis.com/css2?family=Roboto+Condensed:wght@300;400;700&display=swap" rel="stylesheet">
<style>
:root{
  --blue:#1c4f86;
  --blue-dark:#163f6b;
  --orange:#f7941d;
  --text:#5a5a5a;
  --heading:#4a4a4a;
  --grey:#8a8a8a;
  --panel:#e4e4e4;
  --footer:#e6e6e6;
  --rule:#c9c9c9;
  --white:#ffffff;
  --black:#111111;
}
*{box-sizing:border-box;margin:0;padding:0}
html,body{width:1054px;height:1200px;overflow:hidden}
body{position:relative;background:var(--white);font-family:"Roboto Condensed",Arial,sans-serif;color:var(--text)}
.abs{position:absolute}

/* header */
.brand{left:150px;top:28px}
.brand-name{font-size:34px;font-weight:400;color:var(--blue);letter-spacing:.5px;line-height:34px;display:flex;align-items:center;gap:7px}
.brand-dot{width:12px;height:12px;border-radius:50%;background:var(--orange)}
.brand-tag{font-size:11.5px;letter-spacing:2.6px;color:var(--blue);margin-top:3px}
.btn{display:inline-flex;align-items:center;justify-content:center;background:var(--blue);color:var(--white);font-size:12px;border-radius:2px;height:22px}
.btn-grey{background:#8c8c8c}
.signup{left:745px;top:22px;width:63px}
.register{left:823px;top:22px;width:80px;gap:8px}
.nav{left:490px;top:56px;display:flex;gap:22px;font-size:16px;color:var(--blue);font-weight:300}
.nav span{position:relative;padding-bottom:8px}
.nav .active{color:var(--orange)}
.nav .active::after{content:"";position:absolute;left:-3px;right:-3px;bottom:0;height:2px;background:var(--blue)}
.nav .active::before{content:"";position:absolute;left:50%;bottom:-5px;margin-left:-4px;border:4px solid transparent;border-top-color:var(--blue);border-bottom:0}

/* hero */
.hero{left:0;top:94px;width:1054px;height:368px;background:linear-gradient(90deg,#d6dbe0 0%,#c8c2bb 28%,#a98f77 45%,#c4c0ba 62%,#dde2e7 80%,#cfd5db 100%)}
.hero-caption{left:543px;top:142px;width:223px;height:111px;background:rgba(17,17,17,.92);padding:13px 15px}
.hero-caption h2{color:var(--orange);font-size:15px;font-weight:700;margin-bottom:6px}
.hero-caption p{color:var(--white);font-size:11px;line-height:16.5px}
.pager{left:798px;top:442px;display:flex;gap:2px}
.pager span{width:17px;height:20px;background:var(--black);color:var(--orange);font-size:11px;font-weight:700;display:flex;align-items:center;justify-content:center}
.pager .on{background:var(--orange);color:var(--white)}

/* welcome */
.welcome{left:150px;top:484px;width:517px}
.welcome h1{color:var(--orange);font-size:16px;font-weight:700;padding-bottom:6px;border-bottom:1px solid var(--rule);margin-bottom:7px}
.welcome p{font-size:9.4px;line-height:15px;margin-bottom:6px}
.welcome .btn{position:absolute;right:0;top:138px;width:57px}

.converter{left:689px;top:487px;width:214px;height:155px;background:var(--panel);padding:6px 22px}
.converter h3{color:var(--orange);font-size:15.5px;font-weight:700;margin-bottom:5px}
.select{height:24px;background:var(--white);margin-bottom:8px;display:flex;font-size:9px;color:#333}
.select span{flex:1;display:flex;align-items:center;justify-content:center}
.select i{width:22px;background:var(--blue);display:flex;align-items:center;justify-content:center}
.amount{height:24px;background:var(--white);font-size:9.5px;color:#333;padding:7px 8px;margin-bottom:9px}
.converter .btn{width:84px;height:25px;font-size:14px}

/* features */
.feature{top:665px;width:190px}
.feature .head{display:flex;align-items:center;gap:6px;margin-bottom:6px}
.feature .icon{width:51px;height:48px;background:#8e8e8e;display:flex;align-items:center;justify-content:center}
.feature .icon.blue{background:var(--blue)}
.feature h4{font-size:15.5px;font-weight:400;color:#777}
.feature h4.strong{color:var(--blue);font-weight:700}
.feature .sub{color:var(--orange);font-size:10.5px;margin-bottom:3px}
.feature p{font-size:9.3px;line-height:13.6px;margin-bottom:11px}
.feature .btn{width:57px;height:21px;font-size:10px}

.divider{left:150px;top:829px;width:753px;height:1px;background:var(--rule)}

/* testimonial */
.portrait{left:150px;top:852px;width:98px;height:98px;border:2px solid var(--blue);background:linear-gradient(160deg,#e3e5e8,#9aa0a8 60%,#3c3f44)}
.quote{left:264px;top:851px;width:352px}
.quote h5{color:var(--blue);font-size:12.2px;font-weight:400;line-height:15.5px;margin-bottom:4px}
.quote p{font-size:9.2px;line-height:15px}
.person{left:150px;top:955px}
.person .name{font-size:14px;color:var(--heading);font-weight:300}
.person .role{font-size:10.5px;color:#333;margin-top:4px}
.person .note{font-size:9px;margin-top:8px}
.dots{left:553px;top:980px;display:flex;gap:4px}
.dots span{width:7px;height:7px;border-radius:50%;background:#9a9a9a}
.dots .on{background:var(--blue)}
.video{left:650px;top:852px;width:253px;height:165px;background:linear-gradient(135deg,#2b2b2b,#161616 55%,#262626)}

/* footer */
.footer{left:0;top:1038px;width:1054px;height:162px;background:var(--footer)}
.f-brand{left:150px;top:1087px}
.f-brand .brand-name{font-size:19px;line-height:20px;gap:5px}
.f-brand .brand-dot{width:8px;height:8px}
.f-brand .brand-tag{font-size:6.5px;letter-spacing:1.4px;margin-top:1px}
.f-legal{left:150px;top:1119px;font-size:9.5px;line-height:14px;color:#444}
.socials{left:151px;top:1153px;display:flex;gap:4px}
.socials span{width:19px;height:19px;background:#9c9c9c;border-radius:2px}
.socials .first{background:var(--blue)}
.f-col{top:1051px}
.f-col h6{font-size:14px;font-weight:300;color:#555;margin-bottom:8px}
.f-col li{list-style:none;font-size:9.3px;line-height:15.1px;color:#555}
.f-col li.active{color:#1e88e5}
.contact li{display:flex;gap:10px;margin-bottom:12px;line-height:14.5px}
.contact svg{flex:none;margin-top:2px}
</style>
</head>
<body>

<header>
  <div class="abs brand">
    <div class="brand-name"><span class="brand-dot"></span>MERIDALE EXCHANGE</div>
    <div class="brand-tag">INTERNATIONAL MONEY TRANSFER</div>
  </div>
  <span class="abs btn signup">Sign Up</span>
  <span class="abs btn register">Register
    <svg width="9" height="9" viewBox="0 0 10 10"><circle cx="5" cy="5" r="5" fill="#fff"/><path d="M4 2.8L7 5 4 7.2z" fill="#1c4f86"/></svg>
  </span>
  <nav class="abs nav">
    <span class="active">Home</span><span>About</span><span>Services</span><span>Transfer</span><span>Money</span><span>FAQ</span><span>Contact</span>
  </nav>
</header>

<section>
  <div class="abs hero" role="img" aria-label="Photo of a smiling woman at a laptop holding a bank card, bright office window behind"></div>
  <div class="abs hero-caption">
    <h2>How to Work Meridale Exchange</h2>
    <p>Lorem ipsum dolor sit amet, consectetur adipiscing elit. Donec nec dignissim lorem. Vestibulum odio ante, malesuada ac auctor vitae, mollis tempus dolor</p>
  </div>
  <div class="abs pager"><span class="on">1</span><span>2</span><span>3</span><span>4</span><span>5</span></div>
</section>

<section class="abs welcome">
  <h1>Welcome to Meridale Exchange</h1>
  <p>Lorem ipsum dolor sit amet, consectetur adipiscing elit. Donec nec dignissim lorem. Vestibulum odio ante, malesuada ac auctor vitae, mollis tempus dolor. Praesent tincidunt felis eget dui consequat consectetur. Maecenas enim ipsum, vulputate sit amet posuere et, rutrum at neque. Morbi suscipit justo tellus, eu dictum metus ultrices nec. Suspendisse at ipsum suscipit nunc placerat porttitor. Integer eget lobortis nulla. Etiam scelerisque neque et cursus vehicula. Sed sed lobortis ante, sed commodo eros. Fusce eget dictum tellus.</p>
  <p>Nam at nulla laoreet, fringilla mi id, fringilla felis. Curabitur blandit, libero vitae scelerisque sollicitudin, lorem magna molestie magna, vel tempor velit lorem vel leo. Lorem ipsum dolor sit amet, consectetur adipiscing elit. Donec nec dignissim lorem. Vestibulum odio ante, malesuada ac auctor vitae, mollis tempus dolor.</p>
  <span class="btn">Read More</span>
</section>

<aside class="abs converter">
  <h3>Currency Converter</h3>
  <div class="select"><span>---------- Transfer From ----------</span><i><svg width="8" height="6"><path d="M0 0h8L4 6z" fill="#fff"/></svg></i></div>
  <div class="select"><span>------------ Transfer to------------</span><i><svg width="8" height="6"><path d="M0 0h8L4 6z" fill="#fff"/></svg></i></div>
  <div class="amount">0000</div>
  <span class="btn">Converter</span>
</aside>

<section>
  <div class="abs feature" style="left:150px">
    <div class="head"><div class="icon blue"><svg width="26" height="30" viewBox="0 0 26 30"><path d="M6 13V9a7 7 0 0 1 14 0v4" fill="none" stroke="#fff" stroke-width="3"/><rect x="2" y="13" width="22" height="16" rx="2" fill="#fff"/><circle cx="13" cy="20" r="2.5" fill="#1c4f86"/><rect x="12" y="21" width="2" height="5" fill="#1c4f86"/></svg></div><h4 class="strong">Safe And Secure</h4></div>
    <div class="sub">Maecenas suscipit tincidunt posuere</div>
    <p>Lorem ipsum dolor sit amet, consectetur adipiscing elit. Donec nec dignissim lorem. Vestibulum odio ante, malesuada ac auctor</p>
    <span class="btn">Read More</span>
  </div>
  <div class="abs feature" style="left:342px">
    <div class="head"><div class="icon"><svg width="34" height="28" viewBox="0 0 34 28"><g fill="#fff"><rect x="2" y="20" width="12" height="3"/><rect x="2" y="15" width="12" height="3"/><rect x="2" y="10" width="12" height="3"/><rect x="16" y="22" width="14" height="3"/><rect x="16" y="17" width="14" height="3"/><circle cx="24" cy="8" r="7"/></g><text x="24" y="12" font-size="10" text-anchor="middle" fill="#8e8e8e" font-family="Arial,sans-serif">$</text></svg></div><h4>Larger Money</h4></div>
    <div class="sub">Maecenas suscipit tincidunt posuere</div>
    <p>Lorem ipsum dolor sit amet, consectetur adipiscing elit. Donec nec dignissim lorem. Vestibulum odio ante, malesuada ac auctor</p>
    <span class="btn btn-grey">Read More</span>
  </div>
  <div class="abs feature" style="left:534px">
    <div class="head"><div class="icon"><svg width="30" height="30" viewBox="0 0 30 30"><circle cx="15" cy="10" r="7" fill="#fff"/><path d="M2 30c0-8 6-12 13-12s13 4 13 12z" fill="#fff"/></svg></div><h4>Custmor Service</h4></div>
    <div class="sub">Maecenas suscipit tincidunt posuere</div>
    <p>Lorem ipsum dolor sit amet, consectetur adipiscing elit. Donec nec dignissim lorem. Vestibulum odio ante, malesuada ac auctor</p>
    <span class="btn btn-grey">Read More</span>
  </div>
  <div class="abs feature" style="left:726px">
    <div class="head"><div class="icon"><svg width="32" height="28" viewBox="0 0 32 28"><rect x="1" y="1" width="30" height="19" fill="none" stroke="#fff" stroke-width="2.5"/><rect x="13" y="20" width="6" height="4" fill="#fff"/><rect x="8" y="24" width="16" height="2.5" fill="#fff"/></svg></div><h4>Online Transfer</h4></div>
    <div class="sub">Maecenas suscipit tincidunt posuere</div>
    <p>Lorem ipsum dolor sit amet, consectetur adipiscing elit. Donec nec dignissim lorem. Vestibulum odio ante, malesuada ac auctor</p>
    <span class="btn btn-grey">Read More</span>
  </div>
</section>

<div class="abs divider"></div>

<section>
  <div class="abs portrait" role="img" aria-label="Portrait photo of a smiling customer in a suit"></div>
  <div class="abs quote">
    <h5>Lorem ipsum dolor sit amet, consectetur adipiscing elit. Donec nec dignissim lorem. Vesti ulum odio ante malesuada ac auctor vitae,</h5>
    <p>Lorem ipsum dolor sit amet, consectetur adipiscing elit. Donec nec dignissim lorem. Vestibulum odio ante, malesuada ac auctor vitae, mollis tempus dolor. Praesent tincidunt felis eget dui consequat consectetur. Maecenas enim ipsum, vulputate sit amet posuere et, rutrum at neque.</p>
  </div>
  <div class="abs person">
    <div class="name">Lorem Ispum Dolor</div>
    <div class="role">Transfers Money between the Uk and France</div>
    <div class="note">(Lorem ipsum dolor sit amet )</div>
  </div>
  <div class="abs dots"><span class="on"></span><span></span><span></span><span></span><span></span><span></span></div>

  <div class="abs video" role="img" aria-label="Video still of two people discussing a money transfer"></div>
  <svg class="abs" style="left:650px;top:852px" width="253" height="165" viewBox="0 0 253 165">
    <rect x="109" y="52" width="35" height="35" rx="2" fill="#fff"/>
    <path d="M121 60l14 9.5-14 9.5z" fill="#111"/>
    <rect x="0" y="140" width="253" height="25" fill="#1a1a1a"/>
    <rect x="0" y="137" width="253" height="3" fill="#555"/>
    <rect x="0" y="137" width="16" height="3" fill="#ccc"/>
    <circle cx="16" cy="138.5" r="4" fill="#ddd"/>
    <rect x="12" y="150" width="3" height="10" fill="#888"/><rect x="18" y="150" width="3" height="10" fill="#888"/>
    <path d="M40 153h3l4-4v12l-4-4h-3z" fill="#888"/>
    <text x="63" y="159" font-size="8" fill="#fff" font-family="Roboto Condensed,Arial,sans-serif">0:05 <tspan fill="#999">/ 1:46</tspan></text>
    <circle cx="189" cy="155" r="4" fill="none" stroke="#888" stroke-width="2.5"/>
    <circle cx="208" cy="155" r="3.5" fill="#888"/>
    <rect x="220" y="151" width="10" height="8" fill="none" stroke="#ddd" stroke-width="1.5"/>
    <rect x="213" y="151" width="2" height="8" fill="none"/>
    <rect x="234" y="151" width="0" height="0"/>
    <path d="M243 150v-2h4M249 148h4v2M253 158v2h-4M247 160h-4v-2" stroke="#ddd" stroke-width="1.2" fill="none" transform="translate(-6,1)"/>
  </svg>
</section>

<footer>
  <div class="abs footer"></div>
  <div class="abs f-brand">
    <div class="brand-name"><span class="brand-dot"></span>MERIDALE EXCHANGE</div>
    <div class="brand-tag">INTERNATIONAL MONEY TRANSFER</div>
  </div>
  <div class="abs f-legal">© 2013 Harbourline Holdings Inc.<br>All Rights Reserved</div>
  <div class="abs socials"><span class="first"></span><span></span><span></span><span></span><span></span><span></span></div>

  <div class="abs f-col" style="left:369px">
    <h6>Online Meridale Exchange</h6>
    <ul><li class="active">Home</li><li>About Us</li><li>Money Transfer</li><li>How to use our service</li><li>Currency Converter</li><li>Frequently Asked Questions</li><li>Contact Us</li></ul>
  </div>
  <div class="abs f-col" style="left:551px">
    <h6>Money Matter</h6>
    <ul><li>Lorem ipsum dolor sit amet coctet</li><li>Vradipiscing elit donec nedignisim</li><li>Orem estibulum odio anteauada ac</li><li>Auctor vitae mollis tempusdol</li><li>Praesent tincidunt felis eget dui</li><li>Consequat consectetur aecenas</li><li>Anim ipsum vulputate sit amet</li></ul>
  </div>
  <div class="abs f-col contact" style="left:759px">
    <h6>Contact</h6>
    <ul>
      <li><svg width="11" height="15" viewBox="0 0 11 15"><path d="M5.5 0A5.5 5.5 0 0 0 0 5.5C0 9.5 5.5 15 5.5 15S11 9.5 11 5.5A5.5 5.5 0 0 0 5.5 0z" fill="#1c4f86"/><circle cx="5.5" cy="5.5" r="2" fill="#e6e6e6"/></svg><span>Lorem ipsum dolor sit amet,<br>Coectetur adipiscing elit. Donec<br>Lumodiote,12345678</span></li>
      <li style="margin-top:4px"><svg width="11" height="15" viewBox="0 0 11 15"><path d="M3 0l3 3-2 2c1 2 2 4 4 5l2-2 1 3-2 3C5 13 1 8 0 3z" fill="#1c4f86"/></svg><span>Call : 123.456.7890</span></li>
      <li style="margin-top:4px"><svg width="14" height="10" viewBox="0 0 14 10"><rect width="14" height="10" fill="#1c4f86"/><path d="M0 0l7 6 7-6" stroke="#e6e6e6" fill="none"/></svg><span>Mail : info@meridaleexchange.com</span></li>
    </ul>
  </div>
</footer>

</body>
</html>
```